Tallyleaf Web Design

Create Website Design for Tallyleaf. Tallyleaf is online application for collaboration team work system (task list management). More concept design for this project please find attach file ("tallyleaf website concept.pdf") . But my concept is just describe minimal features not bind design

For tallyleaf logo, i had already attach files. But i had not decided what color i chose, so it's okay if you suggest logo color for your suitable website design.
Updates

Dear All Designer,

I like brisk carousel (http://quorvanlabs.example/brisk-carousel/),
may be your concept design can adjust with this concept.
but don't worry about script for brisk carousel, my team will be handle
You just make website design to suitable with brisk carousel

but if you had own website design concept are welcome

thanks

Target Market(s)

Business Company

Industry/Entity Type

Management

```html
<!DOCTYPE html>
<html lang="en">
<head>
<meta charset="utf-8">
<title>Tallyleaf</title>
<link href="https://fonts.googleapis.com/css2?family=Open+Sans:wght@400;600;700&family=Droid+Sans&display=swap" rel="stylesheet">
<style>
:root{
  --teal:#1b95a6;
  --teal-dark:#18798a;
  --heading:#1f6e79;
  --lime:#a8d63d;
  --panel:#efefef;
  --field:#e3e3e3;
  --text:#333;
  --white:#fff;
}
*{margin:0;padding:0;box-sizing:border-box}
html,body{width:1200px;height:644px;overflow:hidden;background:var(--white);font-family:"Open Sans",sans-serif;color:var(--text)}
.site{position:relative;width:1200px;height:644px}
.header{position:absolute;left:0;top:0;width:1200px;height:77px;background:var(--panel);border-bottom:4px solid var(--lime);height:81px}
.brand{position:absolute;display:flex;align-items:center;gap:8px;color:var(--teal-dark);font-weight:700;letter-spacing:-0.5px}
.brand .dot{width:14px;height:14px;border-radius:50%;background:var(--teal)}
.brand-top{left:318px;top:18px;font-size:36px;line-height:40px}
.brand-bottom{left:312px;top:590px;font-size:25px;line-height:30px}
.brand-bottom .dot{width:10px;height:10px}
.main-nav{position:absolute;left:543px;top:42px;display:flex;gap:20px;font-size:10px;color:var(--text)}
.main-nav a,.footer-nav a{color:inherit;text-decoration:none}
.login{position:absolute;left:845px;top:0;width:42px;height:25px;background:var(--teal);color:var(--white);font-size:10px;display:flex;align-items:center;justify-content:center;border-radius:0 0 5px 5px}
.hero{position:absolute;left:315px;top:98px;width:569px;height:242px;background:var(--panel);border-radius:4px 4px 0 0}
.hero-title{position:absolute;left:40px;top:54px;font-family:"Droid Sans","Open Sans",sans-serif;font-weight:400;font-size:21px;line-height:22px;color:var(--heading);letter-spacing:0.3px}
.hero-art{position:absolute;left:32px;top:142px;width:290px;height:100px;background:linear-gradient(90deg,var(--lime) 0 55%,var(--teal) 55% 100%);border-radius:30px 30px 0 0}
.trial{position:absolute;left:678px;top:118px;width:181px;height:197px;background:var(--white);border:1px solid var(--lime)}
.trial h2{position:absolute;left:23px;top:13px;font-weight:400;font-size:16px;color:var(--heading);white-space:nowrap}
.field{position:absolute;left:23px;width:127px;height:20px;background:var(--field);border-top:2px solid #c9c9c9;font-size:8px;color:#888;padding:3px 8px}
.trial-btn{position:absolute;left:35px;top:152px;width:152px;height:25px;background:var(--teal-dark);color:var(--white);font-weight:700;font-size:12px;border-radius:6px;display:flex;align-items:center;justify-content:center;letter-spacing:0.2px}
.features{position:absolute;left:315px;top:378px;width:575px;display:flex;justify-content:space-between}
.feature{width:165px;text-align:center}
.feature h3{font-family:"Droid Sans","Open Sans",sans-serif;font-size:10px;font-weight:700;color:var(--text);height:20px;line-height:14px}
.feature svg{display:block;margin:0 auto;height:32px}
.feature p{margin-top:8px;font-size:8.3px;line-height:11px;color:var(--text)}
.footer{position:absolute;left:0;top:511px;width:1200px;height:133px;background:var(--panel)}
.footer-nav{position:absolute;left:318px;top:25px;display:flex;gap:20px;font-size:10px}
.social{position:absolute;left:780px;top:20px;display:flex;gap:19px}
.social span{width:20px;height:18px;background:var(--teal-dark);border-radius:3px}
</style>
</head>
<body>
<div class="site">
  <header class="header">
    <div class="brand brand-top"><span>tallyleaf</span><span class="dot"></span></div>
    <nav class="main-nav"><a href="#">Home</a><a href="#">Servises</a><a href="#">Support</a><a href="#">Pricing</a><a href="#">Free Trial</a><a href="#">Contact</a></nav>
    <a class="login">Login</a>
  </header>

  <section class="hero">
    <h1 class="hero-title">Project Management Software<br>that makes your life easier!</h1>
    <div class="hero-art" role="img" aria-label="Illustration of a team of three people beside a computer and a printer"></div>
  </section>

  <form class="trial">
    <h2>Start your free trial</h2>
    <div class="field" style="top:47px">your project</div>
    <div class="field" style="top:77px">name</div>
    <div class="field" style="top:106px">e-mail</div>
    <div class="trial-btn">START YOUR FREE TRIAL</div>
  </form>

  <section class="features">
    <div class="feature">
      <h3>Customize Application</h3>
      <svg viewBox="0 0 34 32" width="34"><path d="M4 10h20V5l8 7-8 7v-5H8v6H4z M30 22H10v5l-8-7 8-7v5h16v-6h4z" fill="var(--teal-dark)"/></svg>
      <p>Jujubes jelly beans pastry cake biscuit jujubes oat cake. Candy canes candy canes topping lemon drops liquorice.</p>
    </div>
    <div class="feature">
      <h3>Synchronize All Device</h3>
      <svg viewBox="0 0 48 30" width="48"><path d="M10 30a10 10 0 0 1 0-19 12 12 0 0 1 22-5 9 9 0 0 1 8 7 9 9 0 0 1 0 17z" fill="var(--teal-dark)"/></svg>
      <p>Jujubes jelly beans pastry cake biscuit jujubes oat cake. Candy canes candy canes topping lemon drops liquorice.</p>
    </div>
    <div class="feature">
      <h3>Report</h3>
      <svg viewBox="0 0 26 30" width="26"><rect x="3" y="1" width="22" height="28" rx="2" fill="var(--teal-dark)"/><rect x="0" y="5" width="5" height="2.5" fill="var(--teal-dark)"/><rect x="0" y="13" width="5" height="2.5" fill="var(--teal-dark)"/><rect x="0" y="21" width="5" height="2.5" fill="var(--teal-dark)"/><rect x="9" y="7" width="12" height="6" fill="#fff"/><rect x="9" y="16" width="12" height="2" fill="#fff"/><rect x="9" y="20" width="12" height="2" fill="#fff"/></svg>
      <p>Jujubes jelly beans pastry cake biscuit jujubes oat cake. Candy canes candy canes topping lemon drops liquorice.</p>
    </div>
  </section>

  <footer class="footer">
    <nav class="footer-nav"><a href="#">Home</a><a href="#">Servises</a><a href="#">Support</a><a href="#">Pricing</a><a href="#">Free Trial</a><a href="#">Contact</a></nav>
    <div class="social"><span></span><span></span><span></span></div>
  </footer>
  <div class="brand brand-bottom"><span>tallyleaf</span><span class="dot"></span></div>
</div>
</body>
</html>
```